Social Media Web Design

We require the design of 3 pages for our social media website. We have designed a general layout, which you can see at the link below:

https://files.quorbelvault.net/folder/d/7KpRt204mWzYuLsHbQnEeTgVxA9/edit?usp=sharing

We need you to design the colour scheme, detailed layout and graphics. We will provide you with three basic HTML pages that will contain text and we would like you to return completed .css files. The html files are only to make your job simpler and to provide details. If it is easier for you to build the .css files from scratch then it is not necessary for you to use them. Also, if you would like to edit the html files feel free. We would like you to focus on the creative design component, specifically colours and graphics.

In terms of colours, we would like to avoid red and blue. We would also prefer not to have various shades of black and dark grey. We like strong, simple design colours that are easy on the eye.
**Update on Colour Themes**
Apologies, I feel that I wasn't entirely clear about the colours, specifically red, blue and black. We'd prefer to stay away from the use of red and blue as a major components of the theme. It is already used quite heavily in other social media sites and we're after a distinct look of our own. I didn't mean to suggest that no red or blue can be used in the design.
***

Some websites that we like the look of include:
https://tindelwisp.com - We particularly like the layout and the colour scheme and contrasts. We would however, prefer to avoid blue themes.
www.gorvabent.com
www.plumeradix.com
www.vastirelon.com - The icons, images and style of this site are really good. As stated above, we'd prefer to avoid black though.

There is no need to design a primary website logo, but please design other icons, buttons and graphics.

We would prefer the page to be bold, modern and fun rather than professional. In addition, we like clean, uncluttered designs and designs that emphasize user experience. The Homepage listed is quite empty in terms of content, so you have freedom to be particularly creative on this page.

If you have any further questions please ask, we are very happy to provide any further details or help you might need.
Updates

Thanks in advance.

Target Market(s)

social media users

Industry/Entity Type

Media

Requirements
Must have
• We require css files at the end of the project.
We require the creation of every field in the design document to complete the project.
The spacial layout must replicate the design document.
Should not have
• Flash, Silverlight

```html
<!DOCTYPE html>
<html lang="en">
<head>
<meta charset="utf-8">
<title>Logo Name – Social Media</title>
<link rel="stylesheet" href="https://fonts.googleapis.com/css2?family=PT+Sans:wght@400;700&display=swap">
<style>
  :root {
    --brand-green: #2f9a58;
    --brand-green-deep: #217a43;
    --search-bg: #26844a;
    --search-border: #1d6b3b;
    --ink-dark: #123222;
    --white: #ffffff;
    --footer-bg: #1f5e37;
    --panel-bg: rgba(47, 154, 88, 0.55);
    --panel-bg-strong: rgba(33, 122, 67, 0.82);
    --panel-border: rgba(255, 255, 255, 0.75);
    --button-top: #f6b332;
    --button-bottom: #e08a12;
    --field-text: #2a2a2a;
    --icon-a: #f6b332;
    --icon-b: #ffffff;
    --icon-c: #a8e0bd;
    --icon-d: #e08a12;
  }
  * { box-sizing: border-box; margin: 0; padding: 0; }
  html, body { width: 1200px; height: 740px; overflow: hidden; }
  body { font-family: "PT Sans", sans-serif; position: relative; background: var(--white); }

  .site-header {
    position: absolute; left: 0; top: 0; width: 1200px; height: 81px;
    background: var(--brand-green);
  }
  .brand { position: absolute; left: 102px; top: 20px; display: flex; align-items: center; gap: 18px; }
  .brand-mark { width: 50px; height: 50px; border-radius: 50%; border: 4px solid var(--white); }
  .brand-name { color: var(--white); font-size: 27px; font-weight: 400; letter-spacing: 0.4px; }

  .search {
    position: absolute; left: 366px; top: 31px; width: 235px; height: 32px;
    background: var(--search-bg); border: 1px solid var(--search-border); border-radius: 6px;
  }
  .search svg { position: absolute; right: 8px; top: 6px; }

  .social-links { position: absolute; left: 1013px; top: 37px; display: flex; gap: 5px; }
  .social-links span { width: 14px; height: 14px; border-radius: 2px; display: block; }
  .social-links span:nth-child(1) { background: var(--icon-a); }
  .social-links span:nth-child(2) { background: var(--icon-b); }
  .social-links span:nth-child(3) { background: var(--icon-c); }
  .social-links span:nth-child(4) { background: var(--icon-d); }

  .hero-photo {
    position: absolute; left: 0; top: 81px; width: 1200px; height: 619px;
    background: linear-gradient(180deg, #eef0ea 0%, #e2dbcf 22%, #c9b5a2 42%, #a9a39c 60%, #7d8a96 78%, #5a5650 100%);
  }

  .tagline { position: absolute; left: 0; top: 263px; }
  .tagline-line {
    display: block; height: 40px; margin-bottom: 1px;
    background: var(--brand-green); color: var(--white);
    font-size: 28px; line-height: 40px; padding-left: 102px; letter-spacing: 0.3px; white-space: nowrap;
  }
  .tagline-line.l1 { width: 583px; }
  .tagline-line.l2 { width: 528px; }
  .tagline-line.l3 { width: 583px; }
  .tagline-line.l4 { width: 285px; }
  .highlight { color: var(--ink-dark); }

  .auth-panel {
    position: absolute; left: 830px; width: 261px;
    border: 3px solid var(--panel-border); border-radius: 8px;
  }
  .login-panel { top: 228px; height: 155px; background: var(--panel-bg); }
  .signup-panel { top: 404px; height: 202px; background: var(--panel-bg-strong); }

  .field {
    position: absolute; height: 27px; background: var(--white);
    color: var(--field-text); font-size: 12px; line-height: 27px; padding-left: 5px;
  }
  .login-panel .field { left: 29px; width: 192px; }
  .signup-panel .field { left: 40px; width: 192px; }

  .btn {
    position: absolute; height: 27px; border-radius: 6px;
    background: linear-gradient(180deg, var(--button-top), var(--button-bottom));
    color: var(--white); font-size: 16px; text-align: center; line-height: 27px;
  }
  .login-panel .btn { left: 144px; top: 103px; width: 78px; }
  .signup-panel .btn { left: 148px; top: 159px; width: 86px; }

  .site-footer {
    position: absolute; left: 0; top: 700px; width: 1200px; height: 40px;
    background: var(--footer-bg); color: var(--white); font-size: 12px; font-weight: 700;
  }
  .copyright { position: absolute; left: 117px; top: 13px; }
  .footer-nav { position: absolute; right: 112px; top: 13px; display: flex; gap: 14px; }
  .footer-nav .sep { font-weight: 400; }
</style>
</head>
<body>
  <header class="site-header">
    <div class="brand">
      <span class="brand-mark"></span>
      <span class="brand-name">Logo Name</span>
    </div>
    <div class="search">
      <svg width="20" height="20" viewBox="0 0 20 20" aria-hidden="true">
        <circle cx="8" cy="8" r="6" fill="none" stroke="#fff" stroke-width="2"/>
        <line x1="12.5" y1="12.5" x2="18" y2="18" stroke="#fff" stroke-width="2.5" stroke-linecap="round"/>
      </svg>
    </div>
    <nav class="social-links" aria-label="Social links">
      <span></span><span></span><span></span><span></span>
    </nav>
  </header>

  <div class="hero-photo" role="img" aria-label="Photo of a family of three generations sitting together on a sofa, looking at tablets"></div>

  <p class="tagline">
    <span class="tagline-line l1">Before social networking, the <span class="highlight">World</span></span>
    <span class="tagline-line l2"><span class="highlight">Wide Web</span> was full of interesting</span>
    <span class="tagline-line l3">mation, but there was little opporthy</span>
    <span class="tagline-line l4">to contribute.</span>
  </p>

  <form class="auth-panel login-panel">
    <div class="field" style="top:22px">Email:</div>
    <div class="field" style="top:62px">Password:</div>
    <div class="btn">Login</div>
  </form>

  <form class="auth-panel signup-panel">
    <div class="field" style="top:31px">Email:</div>
    <div class="field" style="top:71px">Password:</div>
    <div class="field" style="top:115px">Confirm Password:</div>
    <div class="btn">Sign Up</div>
  </form>

  <footer class="site-footer">
    <span class="copyright">© 2012 - 2013 Social Media Company.</span>
    <nav class="footer-nav">
      <span>About</span><span class="sep">|</span>
      <span>Developers</span><span class="sep">|</span>
      <span>Blog</span><span class="sep">|</span>
      <span>Help</span>
    </nav>
  </footer>
</body>
</html>
```